Fresh pet feed direct from manufacturer to door step. Quality and Freshness un-surpassed in Industr

Need Business Card Design; leading into many other projects, for New Franchised Business Opportunity providing home delivery of fresh dog and cat feed (no emphasis needed for cat) direct from manufacturing facility. (no middle men or distributors) Food is Farm to Factory fresh. Our trademarked tagline is "Quality is our MAIN Ingredient ! "
Updates

Please take note of other contest for Chirplane Cover and Profile Pic's

Target Market(s)

Dog and Cat owners

Industry/Entity Type

Pet

Contact Information for Business Card

Name, address, local phone, national 800 number, website, email address

Other font styles liked:
• follow that from logo

Requirements
Must have
• Our feed is made in Texas with ingredients sourced from local farms. We want to lean heavy on the Made in West Texas , ranch theme but that has a 'black label', 'vantrel', 'premium', 'high-end' look and feel
Nice to have
• maybe have an offer on card? 20% off with promo code "x" etc.. ?? just a thought...

```html
<!DOCTYPE html>
<html lang="en">
<head>
<meta charset="utf-8">
<title>Hollis Premium – Business Card</title>
<link rel="stylesheet" href="https://fonts.googleapis.com/css2?family=Cinzel:wght@700&family=Old+Standard+TT:wght@700&display=swap">
<style>
  :root {
    --stage: #d8d5cf;
    --ink: #0b0b0d;
    --paper: #f4f4f4;
    --paper-shade: #dcdcdc;
    --gold: #d8a928;
    --gold-light: #f3d36a;
    --white: #ffffff;
    --mist: #d2d2d2;
    --paw-grey: #bdbdbd;
  }
  html, body {
    margin: 0;
    width: 1200px;
    height: 1200px;
    overflow: hidden;
    background: var(--stage);
  }
  .canvas { position: relative; width: 1200px; height: 1200px; }
  .card {
    position: absolute;
    left: 150px;
    width: 900px;
    height: 514px;
    box-shadow: 0 10px 28px rgba(0,0,0,.28);
  }
  .card--front { top: 56px; }
  .card--back  { top: 630px; }
  .card svg { display: block; width: 900px; height: 514px; }
  .brand-name { font-family: "Cinzel", serif; font-weight: 700; fill: var(--white); }
  .holder-name, .holder-title { font-family: "Cinzel", serif; font-weight: 700; fill: var(--gold); }
  .contact-text { font-family: "Old Standard TT", serif; font-weight: 700; fill: var(--ink); font-size: 21px; }
  .icon-at { font-family: "Old Standard TT", serif; font-weight: 700; fill: var(--white); font-size: 22px; }
</style>
</head>
<body>
<main class="canvas">

  <section class="card card--front" aria-label="Business card front">
    <svg viewBox="0 0 900 514" xmlns="http://www.w3.org/2000/svg">
      <defs>
        <linearGradient id="paperGrad" x1="0" y1="0" x2="1" y2="1">
          <stop offset="0" stop-color="var(--paper)"/>
          <stop offset="1" stop-color="var(--paper-shade)"/>
        </linearGradient>
        <linearGradient id="goldGrad" x1="0" y1="0" x2="1" y2="0">
          <stop offset="0" stop-color="var(--gold)"/>
          <stop offset=".5" stop-color="var(--gold-light)"/>
          <stop offset="1" stop-color="var(--gold)"/>
        </linearGradient>
      </defs>
      <rect class="paper" width="900" height="514" fill="url(#paperGrad)"/>

      <path class="sweep sweep--top" d="M520,0 H900 V235 C820,115 690,35 520,0 Z" fill="var(--ink)"/>
      <path class="sweep-edge" d="M505,0 C690,38 820,112 900,246" fill="none" stroke="url(#goldGrad)" stroke-width="8"/>
      <path class="sweep sweep--bottom" d="M0,295 C120,430 290,500 430,514 H0 Z" fill="var(--ink)"/>
      <path class="sweep-edge" d="M0,282 C120,425 290,498 445,514" fill="none" stroke="url(#goldGrad)" stroke-width="8"/>

      <path class="ribbon ribbon--left" d="M40,235 H240 V335 H40 L92,285 Z" fill="var(--ink)" stroke="var(--gold)" stroke-width="5"/>
      <path class="ribbon ribbon--right" d="M860,190 H660 V290 H860 L808,240 Z" fill="var(--ink)" stroke="var(--gold)" stroke-width="5"/>

      <ellipse class="emblem" cx="450" cy="257" rx="255" ry="142" fill="var(--ink)" stroke="url(#goldGrad)" stroke-width="8"/>
      <circle class="brand-dot" cx="290" cy="258" r="32" fill="var(--white)"/>
      <text class="brand-name" x="478" y="262" font-size="64" text-anchor="middle">HOLLIS</text>
      <text class="brand-name" x="478" y="302" font-size="26" text-anchor="middle">PREMIUM</text>
    </svg>
  </section>

  <section class="card card--back" aria-label="Business card back">
    <svg viewBox="0 0 900 514" xmlns="http://www.w3.org/2000/svg">
      <defs>
        <linearGradient id="goldGradB" x1="0" y1="0" x2="0" y2="1">
          <stop offset="0" stop-color="var(--gold)"/>
          <stop offset=".5" stop-color="var(--gold-light)"/>
          <stop offset="1" stop-color="var(--gold)"/>
        </linearGradient>
        <linearGradient id="mistGrad" x1="0" y1="0" x2="1" y2="1">
          <stop offset="0" stop-color="var(--paper)"/>
          <stop offset=".55" stop-color="var(--mist)"/>
          <stop offset="1" stop-color="var(--paw-grey)"/>
        </linearGradient>
      </defs>
      <rect class="panel--dark" width="900" height="514" fill="var(--ink)"/>

      <path class="panel--light" role="img" aria-label="Faint grey paw print pattern across the light panel" d="M0,0 H440 C470,150 420,360 160,514 H0 Z" fill="url(#mistGrad)"/>
      <path class="panel-edge" d="M440,0 C470,150 420,360 160,514" fill="none" stroke="url(#goldGradB)" stroke-width="14"/>

      <ellipse class="emblem" cx="200" cy="190" rx="165" ry="82" fill="var(--ink)" stroke="var(--gold)" stroke-width="6"/>
      <circle class="brand-dot" cx="88" cy="190" r="22" fill="var(--white)"/>
      <text class="brand-name" x="218" y="196" font-size="42" text-anchor="middle">HOLLIS</text>
      <text class="brand-name" x="218" y="228" font-size="17" text-anchor="middle">PREMIUM</text>

      <text class="holder-name" x="690" y="74" font-size="28" text-anchor="middle">HOLLIS PREMIUM</text>
      <line class="holder-rule" x1="570" y1="86" x2="810" y2="86" stroke="var(--gold)" stroke-width="2"/>
      <text class="holder-title" x="690" y="112" font-size="20" text-anchor="middle">YOUR TITLE</text>

      <g class="contact-row">
        <rect x="490" y="168" width="410" height="46" fill="var(--white)"/>
        <circle cx="518" cy="191" r="22" fill="var(--ink)" stroke="var(--white)" stroke-width="3"/>
        <path d="M518,180 a8,8 0 0 1 8,8 c0,6 -8,14 -8,14 c0,0 -8,-8 -8,-14 a8,8 0 0 1 8,-8 z" fill="none" stroke="var(--white)" stroke-width="2.5"/>
        <circle cx="518" cy="188" r="2.5" fill="var(--white)"/>
        <text class="contact-text" x="554" y="198">Company address here</text>
      </g>
      <g class="contact-row">
        <rect x="490" y="228" width="410" height="46" fill="var(--white)"/>
        <circle cx="518" cy="251" r="22" fill="var(--ink)" stroke="var(--white)" stroke-width="3"/>
        <path d="M512,241 l4,-2 l3,7 l-3,2 c1,4 3,7 6,9 l2,-3 l7,3 l-2,4 c-9,1 -18,-9 -17,-20 z" fill="var(--white)"/>
        <text class="contact-text" x="554" y="258">999 - 1234 - 5678</text>
      </g>
      <g class="contact-row">
        <rect x="490" y="288" width="410" height="46" fill="var(--white)"/>
        <circle cx="518" cy="311" r="22" fill="var(--ink)" stroke="var(--white)" stroke-width="3"/>
        <text class="icon-at" x="518" y="318" text-anchor="middle">@</text>
        <text class="contact-text" x="554" y="318">hello@hollispremium.com</text>
      </g>
      <g class="contact-row">
        <rect x="490" y="348" width="410" height="46" fill="var(--white)"/>
        <circle cx="518" cy="371" r="22" fill="var(--ink)" stroke="var(--white)" stroke-width="3"/>
        <g fill="none" stroke="var(--white)" stroke-width="2">
          <circle cx="518" cy="371" r="11"/>
          <ellipse cx="518" cy="371" rx="5" ry="11"/>
          <line x1="507" y1="371" x2="529" y2="371"/>
        </g>
        <text class="contact-text" x="554" y="378">www.hollispremium.com</text>
      </g>
    </svg>
  </section>

</main>
</body>
</html>
```